Website Design for Business Law Firm

We have a logo and now we would like a web site design for our new website. Our small firm provides creative and aggressive transactional (not litigation) legal services to advise healthcare, technology, internet-based and traditional companies and investors in such companies on healthcare, technology, financing, mergers/acquisitions, real estate and other transactions, legal compliance and general corporate and business matters.

We would like to see a website design that is professional and appropriate for executives, professionals, investors and government regulators to visit, that conveys professionalism and competence while being a little edgy and modern - no typical legal motifs such as gavels, books, or scales of justice. We advise businesses and investors and guide them through complicated issues quickly, capably and differently from other law firms. We are part of the business team and get things done.

The logo is attached, and we like gray as a color to complement it. The intention of the logo is to convey that in a storm or challenging time, people come to this firm, and people come to this firm when they need the power and disruption to change things or shake them up.

I have also enclosed a picture of our business card for consideration.

On the other hand, you can check out the current simple site at www.venhollow.example to see we have used a space motif in the past to evoke that we help create stars (the nebula featured there). This is not a necessary part of the new website and it may look better without it.

We appreciate your creativity and look forward to designs.

Industry/Entity Type

Business

Requirements
Must have
• We anticipate the following pages, and you may submit different ideas for the different pages:
• 1. Landing page
• 2. Services pages - healthcare, IT/Technology, general counsel services, financings, mergers/acquisitions, mediation/arbitration, procurement and productization
• 3. About Us including contact information
• Our name and contact information:
• Quellane Law Firm, P.C.
• 8716 SW 19th Ave.
• Portland, OR 97213
• phone: 971.555.0143
• fax: 971.555.0187
Nice to have
• Please consider designs that enhance the impressions we are looking for
Should not have
• Please no gavels, scales of justice, law books, or similar traditional legal imagery.

```html
<!DOCTYPE html>
<html lang="en">
<head>
<meta charset="utf-8">
<title>Quellane Law Firm</title>
<link href="https://fonts.googleapis.com/css2?family=Lato:wght@400;700;900&family=Delius&family=Courgette&display=swap" rel="stylesheet">
<style>
:root{
  --page:#e9e9e9;
  --edge:#d6d6d6;
  --ink:#1e1e1e;
  --text:#4a4a4a;
  --muted:#9a9a9a;
  --dark:#3a3a3a;
  --darker:#2b2b2b;
  --card:#cfcfcf;
  --card-top:#b4b4b4;
  --nav:#d2d2d2;
  --nav-line:#bdbdbd;
  --line:#8a8a8a;
}
*{margin:0;padding:0;box-sizing:border-box}
html,body{width:1200px;height:2206px;overflow:hidden}
body{background:var(--edge);font-family:"Delius",cursive;color:var(--text);position:relative}
.sheet{position:absolute;left:16px;top:0;width:1168px;height:2206px;background:var(--page)}
.abs{position:absolute}
.nav{left:121px;top:0;width:970px;height:52px;display:flex;background:var(--nav)}
.nav a{flex:1;display:flex;align-items:center;justify-content:center;font:400 15px "Lato",sans-serif;color:#555;text-decoration:none;text-transform:uppercase;border-left:1px solid var(--nav-line)}
.nav a.active{background:var(--darker);color:#fff;border-left:none}
.brand{left:121px;top:111px;width:244px;height:60px;display:flex;align-items:center;gap:12px}
.brand-mark{width:46px;height:46px;background:var(--dark)}
.brand-name{font:700 32px "Lato",sans-serif;letter-spacing:5px;color:var(--dark)}
.social{left:1010px;top:135px;display:flex;gap:10px}
.social span{width:36px;height:36px;border-radius:50%;background:#8f8f8f;display:block}
.hero{left:121px;top:196px;width:970px;height:444px;background:linear-gradient(90deg,#a9a4b8 0%,#d9d3cf 35%,#eceae8 60%,#cfd4dc 100%)}
.hero-box{left:834px;top:212px;width:245px;height:364px;background:rgba(58,58,58,.92);padding:52px 22px 0 22px;color:#fff}
.hero-box h2{font:400 25px/1.05 "Lato",sans-serif;text-transform:uppercase;margin-bottom:18px}
.hero-box p{font:400 14px/1.55 "Lato",sans-serif;color:#d8d8d8}
.hero-box .more{display:block;margin-top:20px;font:700 11px "Lato",sans-serif;color:#fff;text-transform:uppercase}
.dots{position:absolute;left:22px;bottom:22px;display:flex;gap:4px}
.dots i{width:18px;height:18px;border-radius:50%;background:#888;display:block}
.dots i.on{background:#fff}
.tagline{left:121px;top:676px;width:740px;white-space:nowrap;font:400 28px/40px "Courgette",cursive;color:var(--ink)}
.btn{left:883px;top:677px;width:206px;height:44px;background:var(--dark);color:#fff;font:700 17px "Lato",sans-serif;display:flex;align-items:center;justify-content:center;text-transform:uppercase}
.card{top:778px;height:379px;background:var(--card);border-top:12px solid var(--card-top);padding:14px 14px 0 14px}
.card h3{font:700 28px "Lato",sans-serif;color:var(--ink);text-transform:uppercase}
.card .photo{width:222px;height:112px;margin:14px auto 0;background:linear-gradient(180deg,#e6e9ee,#b9b2aa)}
.card p{margin-top:24px;font-size:15.5px;line-height:1.2;color:#8a8a8a}
.card .more-btn{position:absolute;left:14px;bottom:14px;width:66px;height:26px;background:var(--dark);color:#fff;font:700 14px "Lato",sans-serif;display:flex;align-items:center;justify-content:center}
.rule{left:121px;width:970px;border-top:2px dotted var(--line)}
.section-title{font:700 30px "Lato",sans-serif;color:var(--ink);text-transform:uppercase}
.solution{top:1354px;width:215px}
.tick{width:40px;height:40px}
.solution h4{margin-top:8px;font:700 29px/1 "Lato",sans-serif;color:var(--ink);text-transform:uppercase;white-space:nowrap}
.solution .sub{font:400 22px "Lato",sans-serif;color:var(--muted);text-transform:uppercase}
.solution p{margin-top:12px;font-size:11.5px;line-height:1.55;color:var(--text)}
.solution .read{display:block;margin-top:30px;text-align:center;font:400 11px "Lato",sans-serif;color:var(--ink);text-transform:uppercase}
.standard{left:121px;top:1772px;width:500px}
.standard-top{display:flex;gap:22px}
.standard-photo{flex:none;width:222px;height:111px;margin-left:4px;background:linear-gradient(180deg,#f2f2f2,#c9c4be)}
.standard-top h3{font:700 24px/1.1 "Lato",sans-serif;color:var(--ink);text-transform:uppercase}
.standard-top .lead{margin-top:4px;font-size:13.5px;line-height:1.3;color:var(--text)}
.standard-body{margin-top:4px;font-size:14px;line-height:1.3;color:var(--text)}
.read-more{display:block;margin-top:14px;font:400 11px "Lato",sans-serif;color:var(--ink);text-transform:uppercase}
.news-item{left:673px;width:396px;display:flex;gap:14px;padding-bottom:14px;border-bottom:2px dotted var(--line)}
.news-item svg{flex:none}
.news-item h5{font:700 10.5px/1.4 "Delius",cursive;color:var(--ink)}
.news-item p{margin-top:6px;font-size:10.5px;line-height:1.5;color:#666}
.foot-line{left:121px;top:2124px;width:970px;border-top:3px solid #9a9a9a}
.foot-social{left:146px;top:2146px;display:flex;gap:10px}
.foot-social span{width:38px;height:38px;border-radius:50%;background:#9a9a9a;display:block}
.foot-nav{left:414px;top:2159px;font:400 12px "Lato",sans-serif;color:#888;text-transform:uppercase}
.foot-nav b{color:var(--ink);font-weight:400}
.copy{left:912px;top:2172px;font:400 12px "Lato",sans-serif;color:#888;text-transform:uppercase}
</style>
</head>
<body>
<div class="sheet"></div>

<nav class="nav abs">
  <a class="active" href="#">Home</a><a href="#">About</a><a href="#">Projects</a><a href="#">Resources</a><a href="#">Contact Us</a>
</nav>

<div class="brand abs"><span class="brand-mark"></span><span class="brand-name">QUELLANE</span></div>
<div class="social abs"><span></span><span></span></div>

<div class="hero abs" role="img" aria-label="Photo of a smiling businesswoman in glasses with colleagues blurred behind"></div>
<div class="hero-box abs">
  <h2>Sed non quam nec tortor molestie</h2>
  <p>Nulla ultricies enim aliquet augue eleifend iaculis. Nam sollicitudin ligula ac nisi iaculis eu scelerisque risus ultricies…</p>
  <span class="more">Read more ▸</span>
  <div class="dots"><i></i><i></i><i class="on"></i></div>
</div>

<div class="tagline abs">Our Work is dedicated to the prosperity of the Clients!</div>
<div class="btn abs">Find out more</div>

<div class="card abs" style="left:121px;width:305px">
  <h3>Resources</h3>
  <div class="photo" role="img" aria-label="Portrait photo of a smiling man"></div>
  <p>Aenean sed fermentum metus. Integer imperdiet nisi vel lectus fermentum malesuada. Aliquam tincidunt tempus tempus. Aliquam euismod malesuada. Aliquam tincidunt tempus tempus. Aliquam euismod</p>
  <span class="more-btn">MORE</span>
</div>
<div class="card abs" style="left:446px;width:303px">
  <h3>Practice</h3>
  <div class="photo" role="img" aria-label="Portrait photo of a businesswoman"></div>
  <p>Aenean sed fermentum metus. Integer imperdiet nisi vel lectus fermentum malesuada. Aliquam tincidunt tempus tempus. Aliquam euismod malesuada. Aliquam tincidunt tempus tempus. Aliquam euismod</p>
  <span class="more-btn">MORE</span>
</div>
<div class="card abs" style="left:772px;width:317px">
  <h3>Cases</h3>
  <div class="photo" role="img" aria-label="Portrait photo of a smiling man in a shirt"></div>
  <p>Aenean sed fermentum metus. Integer imperdiet nisi vel lectus fermentum malesuada. Aliquam tincidunt tempus tempus. Aliquam euismod malesuada. Aliquam tincidunt tempus tempus. Aliquam euismod</p>
  <span class="more-btn">MORE</span>
</div>

<div class="rule abs" style="top:1196px"></div>

<h2 class="section-title abs" style="left:121px;top:1282px">Featured Solutions</h2>

<div class="solution abs" style="left:121px">
  <svg class="tick" viewBox="0 0 40 40"><circle cx="20" cy="20" r="20" fill="#3a3a3a"/><path d="M11 20l6 6 12-12" fill="none" stroke="#fff" stroke-width="4"/></svg>
  <h4>Healthcare</h4><div class="sub">Solutions</div>
  <p>Contrary to popular belief, Lorem Ipsum is not simply random text. It has roots in a piece of classical Latin literature from 45 BC, making it over 2000 years old. Arlen Dovecote, a Latin professor at Marlow Vale College in Ostrand, looked up one of the more</p>
  <span class="read">Read more ▸</span>
</div>
<div class="solution abs" style="left:360px">
  <svg class="tick" viewBox="0 0 40 40"><circle cx="20" cy="20" r="20" fill="#3a3a3a"/><path d="M11 20l6 6 12-12" fill="none" stroke="#fff" stroke-width="4"/></svg>
  <h4>Technology</h4><div class="sub">Solutions</div>
  <p>Contrary to popular belief, Lorem Ipsum is not simply random text. It has roots in a piece of classical Latin literature from 45 BC, making it over 2000 years old. Arlen Dovecote, a Latin professor at Marlow Vale College in Ostrand, looked up one of the more</p>
  <span class="read">Read more ▸</span>
</div>
<div class="solution abs" style="left:616px">
  <svg class="tick" viewBox="0 0 40 40"><circle cx="20" cy="20" r="20" fill="#3a3a3a"/><path d="M11 20l6 6 12-12" fill="none" stroke="#fff" stroke-width="4"/></svg>
  <h4>Financing</h4><div class="sub">Solutions</div>
  <p>Contrary to popular belief, Lorem Ipsum is not simply random text. It has roots in a piece of classical Latin literature from 45 BC, making it over 2000 years old. Arlen Dovecote, a Latin professor at Marlow Vale College in Ostrand, looked up one of the more</p>
  <span class="read">Read more ▸</span>
</div>
<div class="solution abs" style="left:875px">
  <svg class="tick" viewBox="0 0 40 40"><circle cx="20" cy="20" r="20" fill="#3a3a3a"/><path d="M11 20l6 6 12-12" fill="none" stroke="#fff" stroke-width="4"/></svg>
  <h4>Real Estate</h4><div class="sub">Solutions</div>
  <p>Contrary to popular belief, Lorem Ipsum is not simply random text. It has roots in a piece of classical Latin literature from 45 BC, making it over 2000 years old. Arlen Dovecote, a Latin professor at Marlow Vale College in Ostrand, looked up one of the more</p>
  <span class="read">Read more ▸</span>
</div>

<div class="rule abs" style="top:1719px"></div>

<section class="standard abs">
  <div class="standard-top">
    <div class="standard-photo" role="img" aria-label="Photo of a businesswoman seated at a desk"></div>
    <div>
      <h3>We hold national quality standard!</h3>
      <p class="lead">Sed ut perspiciatis unde omnis iste natus error sit voluptatem</p>
    </div>
  </div>
  <p class="standard-body">Lorem Ipsum is simply dummy text of the printing and typesetting industry. Lorem Ipsum has been the industry's standard dummy text ever since the 1500s, when an unknown printer took a galley of type and scrambled it to make a type specimen book. It has survived not only five centuries, but also the leap into electronic typesetting, remaining essentially unchanged. It was popularised in the 1960s with the release of Lettrane sheets containing Lorem Ipsum passages, and more recently with desktop publishing software like Tessel PageForge including versions of Lorem Ipsum.</p>
  <span class="read-more">Read more ▸</span>
</section>

<h2 class="section-title abs" style="left:673px;top:1764px;font-size:27px">Latest News</h2>
<div class="news-item abs" style="top:1804px">
  <svg width="50" height="64" viewBox="0 0 50 64"><path d="M2 2h38l8 8v52H2z" fill="#f4f4f4" stroke="#9a9a9a" stroke-width="2"/><text x="25" y="34" text-anchor="middle" font-family="Lato,sans-serif" font-weight="700" font-size="20" fill="#555">4</text><text x="25" y="52" text-anchor="middle" font-family="Lato,sans-serif" font-weight="700" font-size="14" fill="#555">DEC</text></svg>
  <div><h5>There are many variations of passages of Lorem Ipsum available</h5><p>There are many variations of passages of Lorem Ipsum available, but the majority have suffered alteration in some form, by injected humour, or randomised words which don't look even slightly believable… (READ MORE)</p></div>
</div>
<div class="news-item abs" style="top:1930px">
  <svg width="50" height="64" viewBox="0 0 50 64"><path d="M2 2h38l8 8v52H2z" fill="#f4f4f4" stroke="#9a9a9a" stroke-width="2"/><text x="25" y="34" text-anchor="middle" font-family="Lato,sans-serif" font-weight="700" font-size="20" fill="#555">4</text><text x="25" y="52" text-anchor="middle" font-family="Lato,sans-serif" font-weight="700" font-size="14" fill="#555">DEC</text></svg>
  <div><h5>There are many variations of passages of Lorem Ipsum available</h5><p>There are many variations of passages of Lorem Ipsum available, but the majority have suffered alteration in some form, by injected humour, or randomised words which don't look even slightly believable… (READ MORE)</p></div>
</div>

<div class="foot-line abs"></div>
<div class="foot-social abs"><span></span><span></span><span></span></div>
<div class="foot-nav abs"><b>Home</b> | About us | Projcts | Resources | Contact</div>
<div class="copy abs">© 2013 | Privacy policy</div>
</body>
</html>
```